Create Website for new company called "Verdant Lodge 17"

Verdant Lodge 17 is a new business situated in Southwestern Colorado. We are creating a business that will rent out spaces where clients can grow their own marijuana. Picture a large green house with partitioned spaces that are secured by a lock. Best way to envision this would be to think of a storage business that rents out storage rooms. The difference is that we will be having the units inside a green house ( for growing purposes) Picture a small area that is secured by locks, Picture an area that has the ability to provide state of the art security, cameras etc. We want to focus our efforts on professionals, blue collar workers and end users of marijuana. Our emphasis is in the area of assisting those whom wish to grow their own plants. We want to provide them a safe facility in which to do that. . Keep in mind that we also build custom grow rooms at clients homes and provide a grow pod (lease these) where a small grow unit will be delivered and picked up from our clients whom want to lease a unit for a short amount of time. We have a business card ( just designed) and will send that information to those whom express an interests in this project. We want to be able to sign people up for our services by entering an agreement and signing the agreement while on the internet. We want to provide our services to those whom consume recreational and medical marijuana. This site will need to gather information I.e email addresses so that we can followup with offers. This is a tremendous opportunity for the right designer. We will be creating many more websites as other states come on line and make marijuana legal to consume. Use the business card model for a point of reference of how we envision the concept. That is a business card we just recently printed. The hands and the plant is our logo so far. Open to suggestions. There will be three levels of service. Bronze, Silver, Gold or Platinum. We will also have a retail biz down the road but not at the present time.

Target Market(s)

Ages 21-60

Industry/Entity Type

Medical

Logo Text

Verdant Lodge 17.

Number of Pages Required

5+ page

Requirements
Must have
• Clean appearance not to busy , easily navigable from link to link, page to page. Must have ability down the road to enter into a contractual agreement via the website. Must use our provided logo and example of that is on our business card that will be uploaded here shortly. We would like to have the colors that are on the business card however if you have suggestions or color schemes that you want us to consider that is okay.
Nice to have
• Nice to have a animation of seed to weed and how clients can save a tremendous amount of money growing their own cannabis. Nice to have testimonial page or feedback page. Have a membership component to website,
Should not have
• No flashing lights, etc. Not to busy in terms of animations.

```html
<!DOCTYPE html>
<html lang="en">
<head>
<meta charset="utf-8">
<title>Verdant Lodge 17</title>
<link href="https://fonts.googleapis.com/css2?family=Open+Sans:wght@400;600&family=Roboto:wght@400;500&display=swap" rel="stylesheet">
<style>
:root{
  --green:#1d8a3a;
  --green-bright:#18a20c;
  --green-dark:#1e7346;
  --text:#555;
  --heading:#333;
  --rule:#ececec;
  --footer:#f1f1f1;
}
*{margin:0;padding:0;box-sizing:border-box}
html,body{width:757px;height:1200px;overflow:hidden;background:#fff}
body{position:relative;font-family:"Open Sans",sans-serif;color:var(--text)}
.abs{position:absolute}
.icon-circle{position:absolute;border:1px solid #e3e3e3;border-radius:50%;background:#fff;display:flex;align-items:center;justify-content:center}
.contact-text{font-size:8.5px;line-height:16px;left:142px;top:26px}
.contact-text .phone{color:var(--green);font-size:9px}
.brand{left:258px;top:34px;width:240px;text-align:center}
.brand-name{font-family:"Roboto",sans-serif;font-weight:500;font-size:22px;color:#3a3a3a;letter-spacing:.2px;line-height:24px;white-space:nowrap}
.brand-tag{font-size:6px;color:#555;margin-top:3px;white-space:nowrap}
.search{left:541px;top:32px;width:108px;height:21px;border:1px solid #e2e2e2;font-size:7px;color:#999;padding:5px 7px}
.nav{left:109px;top:82px;width:540px;height:35px;background:linear-gradient(#18ad0d,#139409);border-bottom:2px solid #0f7a09;box-shadow:0 6px 8px -4px rgba(0,0,0,.35);z-index:3}
.nav a{position:absolute;top:11px;color:#fff;font-family:"Roboto",sans-serif;font-size:10.5px;text-decoration:none}
.hero{left:0;top:99px;width:757px;height:357px;background:linear-gradient(180deg,#f4c658 0%,#eed27a 30%,#b8c870 60%,#7fa64a 85%,#5b8a37 100%)}
.slide-title{left:109px;top:223px;width:142px;height:31px;background:var(--green);color:#fff;font-family:"Roboto",sans-serif;font-size:18px;padding:4px 8px}
.slide-caption{left:108px;top:259px;width:254px;height:38px;background:rgba(80,80,70,.55);color:#fff;font-size:8px;line-height:14px;padding:5px 8px;border-radius:2px}
.arrow{top:240px;width:21px;height:21px;border-radius:50%;background:rgba(70,70,70,.45);display:flex;align-items:center;justify-content:center}
.tiles{left:108px;top:395px;width:541px;height:123px;background:#fff;border:1px solid #e4e4e4}
.tile-img{position:absolute;top:3px;width:175px;height:116px}
.feature{width:180px;text-align:center}
.feature h3{font-family:"Roboto",sans-serif;font-weight:400;font-size:10px;color:#444;margin-bottom:12px}
.feature p{font-size:7px;line-height:13px}
.btn{position:absolute;height:22px;border:1px solid var(--green);border-radius:2px;color:var(--green);font-family:"Roboto",sans-serif;font-size:7.5px;display:flex;align-items:center;justify-content:center}
.rule{left:109px;width:540px;height:1px;background:var(--rule)}
.about-img{left:109px;top:674px;width:229px;height:145px;background:linear-gradient(180deg,#b8c6c0 0%,#9fb59b 35%,#3fa13a 60%,#1f7e1a 100%)}
.about h2{font-family:"Roboto",sans-serif;font-weight:400;font-size:20px;line-height:27px}
.about .kicker{color:var(--green)}
.about .title{color:var(--heading)}
.about p{font-size:6.8px;line-height:13px;margin-top:7px;width:295px}
.news-h{left:110px;top:855px;font-family:"Roboto",sans-serif;font-size:17px;color:var(--heading);letter-spacing:.3px}
.news-img{top:887px;width:172px;height:111px;box-shadow:0 5px 7px -4px rgba(0,0,0,.35)}
.news-item{width:173px}
.news-item .date{font-family:"Roboto",sans-serif;font-size:10px;color:var(--green)}
.news-item p{font-size:6.2px;line-height:13px;margin-top:4px}
.footer{left:0;top:1087px;width:757px;height:70px;background:var(--footer)}
.footer-text{font-size:8px;line-height:16px;color:#555}
.social{top:1111px;width:25px;height:25px;border-radius:50%;background:var(--green);display:flex;align-items:center;justify-content:center}
.bottom{left:0;top:1157px;width:757px;height:43px;background:var(--green-dark);color:#fff;font-size:8px}
.bottom .copy{position:absolute;left:109px;top:16px}
.bottom .links{position:absolute;right:108px;top:16px}
</style>
</head>
<body>

<header>
  <div class="icon-circle" style="left:108px;top:27px;width:26px;height:26px">
    <svg width="11" height="11" viewBox="0 0 24 24"><path fill="#1d8a3a" d="M6.6 10.8a15.2 15.2 0 0 0 6.6 6.6l2.2-2.2c.3-.3.7-.4 1-.2 1.1.4 2.3.6 3.6.6.6 0 1 .4 1 1V20c0 .6-.4 1-1 1A17 17 0 0 1 3 4c0-.6.4-1 1-1h3.5c.6 0 1 .4 1 1 0 1.3.2 2.5.6 3.6.1.3 0 .7-.2 1z"/></svg>
  </div>
  <div class="abs contact-text">info@verdantlodge17.com<br><span class="phone">+1 970 555 0117</span></div>
  <div class="abs brand">
    <div class="brand-name">VERDANT LODGE 17</div>
    <div class="brand-tag">“supporting the care &amp; cultivation of cannabis”</div>
  </div>
  <div class="abs search">Search
    <svg class="abs" style="right:7px;top:7px" width="8" height="8" viewBox="0 0 10 10"><circle cx="4" cy="4" r="3" fill="none" stroke="#aaa" stroke-width="1.2"/><path d="M6.3 6.3 9 9" stroke="#aaa" stroke-width="1.2"/></svg>
  </div>
</header>

<nav class="abs nav">
  <a style="left:12px">Home</a>
  <a style="left:74px">What We Do</a>
  <a style="left:170px">Services</a>
  <a style="left:248px">Projects</a>
  <a style="left:324px">News and Events</a>
  <a style="left:441px">Contact Us</a>
</nav>

<section class="abs hero" role="img" aria-label="Field of young cannabis plants against a warm golden sky"></section>
<div class="abs slide-title">Verdant Lodge</div>
<div class="abs slide-caption">Sed ut perspiciatis unde omnis iste natus error sit voluptatem accusantium doloremque laudantium, totam rem aperiam,</div>
<div class="abs arrow" style="left:20px"><svg width="8" height="8" viewBox="0 0 10 10"><path d="M6.5 1 3 5l3.5 4" fill="none" stroke="#fff" stroke-width="1.3"/></svg></div>
<div class="abs arrow" style="left:713px"><svg width="8" height="8" viewBox="0 0 10 10"><path d="M3.5 1 7 5 3.5 9" fill="none" stroke="#fff" stroke-width="1.3"/></svg></div>

<section class="abs tiles">
  <div class="tile-img" style="left:3px;background:linear-gradient(135deg,#2f7d1e,#6fb83a 50%,#2c6a1a)" role="img" aria-label="Close-up of a cannabis leaf"></div>
  <div class="tile-img" style="left:183px;background:linear-gradient(180deg,#e2e6e4 0%,#c7cfca 45%,#5c8f3e 70%,#3e7226 100%)" role="img" aria-label="Interior of a hoop greenhouse with rows of plants"></div>
  <div class="tile-img" style="left:363px;background:linear-gradient(135deg,#8fbf6a,#3f8a2a 55%,#2d5e1c)" role="img" aria-label="Hand holding a cannabis leaf"></div>
</section>

<div class="abs feature" style="left:108px;top:535px"><h3>Nemo enim ipsam volup</h3><p>Lorem ipsum dolor sit amet, consectetur adipisicing elit, sed do eiusmod tempor didunt labore et dolore magna aliqua.</p></div>
<div class="abs feature" style="left:288px;top:535px"><h3>Nemo enim ipsam volup</h3><p>Lorem ipsum dolor sit amet, consectetur adipisicing elit, sed do eiusmod tempor didunt labore et dolore magna aliqua.</p></div>
<div class="abs feature" style="left:468px;top:535px"><h3>Nemo enim ipsam volup</h3><p>Lorem ipsum dolor sit amet, consectetur adipisicing elit, sed do eiusmod tempor didunt labore et dolore magna aliqua.</p></div>
<a class="btn" style="left:169px;top:608px;width:59px">READ MORE</a>
<a class="btn" style="left:349px;top:608px;width:59px">READ MORE</a>
<a class="btn" style="left:529px;top:608px;width:59px">READ MORE</a>

<div class="abs rule" style="top:654px"></div>

<section>
  <div class="abs about-img" role="img" aria-label="Large greenhouse with irrigated rows of green seedlings"></div>
  <div class="abs about" style="left:357px;top:670px">
    <h2 class="kicker">GET TO KNOW MORE</h2>
    <h2 class="title">About Verdant Lodge</h2>
    <p>Nemo enim ipsam voluptatem quia voluptas sit aspernatur aut odit aut fugit, sed quia tur magni dolores eos qui ratione voluptatem sequi nesciunt. Neque porro quisquam est, qui dolorem ipsum quia dolor sit amet, consectetur, adipisci velit, sed quia non numquam eius modi tempora. dolores eos qui ratione voluptatem sequi nesciunt. Neque porro quisquam est, qui dolorem ipsum quia</p>
  </div>
  <a class="btn" style="left:357px;top:799px;width:60px">READ MORE</a>
</section>

<div class="abs rule" style="top:842px"></div>

<section>
  <h2 class="abs news-h" style="font-weight:400">News &amp; Events</h2>
  <div class="abs news-img" style="left:108px;background:linear-gradient(180deg,#8a8a2a,#a9a23a 45%,#5f6a1f)" role="img" aria-label="Rows of mature cannabis plants in a field"></div>
  <div class="abs news-img" style="left:293px;background:linear-gradient(135deg,#4f7a2a,#8aa04a 50%,#c47a5a 70%,#3b6320)" role="img" aria-label="Close-up of a flowering cannabis bud"></div>
  <div class="abs news-img" style="left:478px;background:linear-gradient(180deg,#b8bcb8,#6f8f52 45%,#2f5a22)" role="img" aria-label="Indoor grow room with dense cannabis plants"></div>
  <div class="abs news-item" style="left:108px;top:1012px"><div class="date">Dec 25, 2014</div><p>Lorem ipsum dolor sit amet, consectetuer adipiscing elit, sed diam nonummy nibh euismod tincidunt ut laoreet dolore Lorem ipsum</p></div>
  <div class="abs news-item" style="left:292px;top:1012px"><div class="date">Dec 25, 2014</div><p>Lorem ipsum dolor sit amet, consectetuer adipiscing elit, sed diam nonummy nibh euismod tincidunt ut laoreet dolore Lorem ipsum</p></div>
  <div class="abs news-item" style="left:477px;top:1012px"><div class="date">Dec 25, 2014</div><p>Lorem ipsum dolor sit amet, consectetuer adipiscing elit, sed diam nonummy nibh euismod tincidunt ut laoreet dolore Lorem ipsum</p></div>
</section>

<footer>
  <div class="abs footer"></div>
  <div class="icon-circle" style="left:108px;top:1105px;width:36px;height:36px">
    <svg width="15" height="14" viewBox="0 0 24 22"><path fill="#1d8a3a" d="M12 2 1 11h3v10h6v-6h4v6h6V11h3z"/></svg>
  </div>
  <div class="abs footer-text" style="left:152px;top:1107px">417 Mesa Verde Rd / Cortez<br>Colorado 81321</div>
  <div class="icon-circle" style="left:318px;top:1105px;width:36px;height:36px">
    <svg width="13" height="13" viewBox="0 0 24 24"><path fill="#1d8a3a" d="M6.6 10.8a15.2 15.2 0 0 0 6.6 6.6l2.2-2.2c.3-.3.7-.4 1-.2 1.1.4 2.3.6 3.6.6.6 0 1 .4 1 1V20c0 .6-.4 1-1 1A17 17 0 0 1 3 4c0-.6.4-1 1-1h3.5c.6 0 1 .4 1 1 0 1.3.2 2.5.6 3.6.1.3 0 .7-.2 1z"/></svg>
  </div>
  <div class="abs footer-text" style="left:362px;top:1107px">Phone No : +1 970 555 0142<br>Email: verdantlodge17.com</div>
  <a class="abs social" style="left:543px" aria-label="Email us">
    <svg width="11" height="9" viewBox="0 0 22 16"><rect x="1" y="1" width="20" height="14" fill="none" stroke="#fff" stroke-width="2"/><path d="M1 1l10 8 10-8" fill="none" stroke="#fff" stroke-width="2"/></svg>
  </a>
  <a class="abs social" style="left:570px" aria-label="Website">
    <svg width="11" height="11" viewBox="0 0 20 20"><circle cx="10" cy="10" r="8" fill="none" stroke="#fff" stroke-width="1.8"/><path d="M2 10h16M10 2c-3 3-3 13 0 16M10 2c3 3 3 13 0 16" fill="none" stroke="#fff" stroke-width="1.5"/></svg>
  </a>
  <a class="abs social" style="left:597px" aria-label="Share">
    <svg width="11" height="11" viewBox="0 0 20 20"><circle cx="15" cy="4" r="2.5" fill="#fff"/><circle cx="5" cy="10" r="2.5" fill="#fff"/><circle cx="15" cy="16" r="2.5" fill="#fff"/><path d="M15 4 5 10l10 6" fill="none" stroke="#fff" stroke-width="1.6"/></svg>
  </a>
  <a class="abs social" style="left:624px" aria-label="Location">
    <svg width="9" height="12" viewBox="0 0 14 20"><path d="M7 1a6 6 0 0 0-6 6c0 5 6 12 6 12s6-7 6-12a6 6 0 0 0-6-6z" fill="#fff"/><circle cx="7" cy="7" r="2.2" fill="#1d8a3a"/></svg>
  </a>
  <div class="abs bottom">
    <span class="copy">© 2014 verdantlodge17.com. All rights reserved.</span>
    <span class="links">Home &nbsp;/ &nbsp;About Us &nbsp;/ &nbsp;Services &nbsp;/ Contact Us</span>
  </div>
</footer>

</body>
</html>
```